Maple construction of ny Roofing flyer

We would like to create a flyer for roofing customers : commercial / real estate management / business / schools /warehouses

Flat roof specialists
Waterproofing experts

Special flat roof re layer @ 3.00 per sq ft

Roof leak repairs
Flashing
Waterproofing

Call 555 2719364

For pictures find torch down roof applications
Flat roofs ny

```html
<!DOCTYPE html>
<html lang="en">
<head>
<meta charset="utf-8">
<title>Maple Construction of NY – Roofing Flyer</title>
<link rel="stylesheet" href="https://fonts.googleapis.com/css2?family=Anton&display=swap">
<style>
  :root {
    --green: #143d22;
    --red: #ff4a3d;
    --white: #ffffff;
    --backdrop: #e9e9e9;
    --roof-dark: #5f8fc2;
    --roof-light: #c4d5e6;
  }
  * { margin: 0; padding: 0; box-sizing: border-box; }
  html, body {
    width: 1200px; height: 827px; overflow: hidden;
    background: var(--backdrop);
  }
  .flyer {
    position: absolute; left: 298px; top: 23px;
    width: 604px; height: 780px;
    background: var(--white);
    font-family: "Anton", "Arial Narrow", sans-serif;
    color: var(--green);
    overflow: hidden;
  }
  .flyer-shapes { position: absolute; inset: 0; width: 100%; height: 100%; }
  .brand { position: absolute; left: 40px; top: 34px; width: 120px; text-align: center; }
  .brand-mark { width: 36px; height: 36px; background: var(--green); margin: 0 auto 8px; }
  .brand-name { font-size: 34px; line-height: 36px; letter-spacing: 2px; text-transform: uppercase; }
  .brand-sub { font-size: 9px; line-height: 12px; letter-spacing: 1px; text-transform: uppercase; }
  .headline {
    position: absolute; left: 184px; top: 50px;
    font-size: 39px; line-height: 48px; font-weight: 400;
    text-transform: uppercase; white-space: nowrap;
  }
  .offer {
    position: absolute; right: 28px; top: 450px;
    color: var(--white); text-align: right;
  }
  .offer-label { font-size: 18px; line-height: 23px; }
  .offer-price { font-size: 74px; line-height: 78px; margin-top: 6px; }
  .offer-unit { font-size: 18px; line-height: 18px; margin-top: -8px; }
  .services {
    position: absolute; left: 64px; top: 555px;
    list-style: none; font-size: 36px; line-height: 47px;
  }
  .footer {
    position: absolute; left: 0; bottom: 0; width: 100%; height: 68px;
    background: var(--green); color: var(--white);
    display: flex; align-items: center; justify-content: center;
    font-size: 37px;
  }
</style>
</head>
<body>
  <article class="flyer">
    <svg class="flyer-shapes" viewBox="0 0 849 1097" preserveAspectRatio="none" aria-hidden="false">
      <defs>
        <linearGradient id="roofTone" x1="0" y1="1" x2="1" y2="0">
          <stop offset="0" stop-color="var(--roof-light)"/>
          <stop offset="0.5" stop-color="var(--roof-dark)"/>
          <stop offset="1" stop-color="var(--roof-light)"/>
        </linearGradient>
      </defs>
      <polygon class="roof-photo" role="img"
        aria-label="Photo: gloved hand rolling black waterproof coating onto a flat roof"
        points="0,260 849,228 849,562 280,710 0,778" fill="url(#roofTone)"/>
      <polygon class="offer-band" points="280,710 849,562 849,955" fill="var(--red)"/>
    </svg>

    <div class="brand">
      <div class="brand-mark"></div>
      <div class="brand-name">Maple</div>
      <div class="brand-sub">Construction of NY</div>
    </div>

    <h1 class="headline">Flat Roof Specialists<br>Waterproofing Experts</h1>

    <div class="offer">
      <p class="offer-label">Special flat<br>roof re layer</p>
      <p class="offer-price">@ 3.00</p>
      <p class="offer-unit">per sq ft</p>
    </div>

    <ul class="services">
      <li>Roof leak repairs</li>
      <li>Flashing</li>
      <li>Waterproofing</li>
    </ul>

    <footer class="footer">Call 555 2719364</footer>
  </article>
</body>
</html>
```